Bramble Roofing & Waterproofing HOA & Commercial Roofing Specialists

FRONT COVER (Panel 1)
Bramble Roofing & Waterproofing
HOA & Commercial Roofing Specialists
Protecting Communities.
Preserving Property Value.
Delivering Long-Term Solutions.
📍 Serving Orange County & Surrounding Areas
INSIDE LEFT PANEL (Panel 2)
Who We Are
Bramble Roofing & Waterproofing is a trusted HOA and commercial roofing specialist serving Orange County and surrounding areas. We understand the unique needs of homeowner associations, property managers, and commercial properties—delivering reliable service, clear communication, and long-lasting results.
✔ HOA-Focused Expertise
✔ Licensed & Insured
✔ Emergency Response Available
✔ Quality Workmanship You Can Trust
INSIDE MIDDLE PANEL (Panel 3)
Roofing Services
HOA & Commercial Roofing
• Emergency roof tarping & repairs — Starting at $550
• Small & large roof repairs
• Chimney cap and spark arrestor repairs
• Preventative roof maintenance
• Roof cleaning
• Full roof replacement
We work on all roof types:
✔ Flat Roofs (Torch down, TPO, & PVC)
✔ Tile Roofs (Clay tiles, concrete tiles, and more)
✔ Shingle Roofs - KTV certified contractor
• Coating (silicone or acrylic)
No matter the size or system—we’ve got you covered.
INSIDE RIGHT PANEL (Panel 4)
Gutter Services
• Small & large gutter repairs
• Gutter cleaning & maintenance
• New gutter installation & replacement
Proper drainage protects your building—let us handle it.
BACK LEFT PANEL (Panel 5)
Deck/Balcony Waterproofing Services
• Balcony/deck maintenance
• Deck resurfacing
• Small & large deck repairs
• Full deck reconstruction
Specialized waterproofing solutions to keep decks safe, compliant, and durable.
BACK COVER (Panel 6)
Why Choose Bramble?
✔ HOA & Commercial Specialists
✔ Fully Licensed & Insured
✔ Reliable Scheduling
✔ Clear Communication
✔ Quality Materials & Craftsmanship
License Information:
C-39 Roofing Contractor
General B Contractor
License #5372941
📍 Office Location:
41 Tolliver Street, Suite D Irvine, CA 92604
📞 Contact us today for a consultation
949-555-0162 or rfp@bramblecrest.example
🌐 Serving Orange County & surrounding areas
- Gotham

```html
<!DOCTYPE html>
<html lang="en">
<head>
<meta charset="utf-8">
<title>Bramble Roofing &amp; Waterproofing – Services Brochure</title>
<link href="https://fonts.googleapis.com/css2?family=Montserrat:wght@400;500;600;700;800&display=swap" rel="stylesheet">
<style>
  :root {
    --ink: #000000;
    --paper: #ffffff;
    --brand-blue: #00a6ea;
    --muted: #d2d2d2;
    --rule: #5a5a5a;
  }
  * { box-sizing: border-box; margin: 0; padding: 0; }
  html, body { width: 1200px; height: 848px; overflow: hidden; background: var(--paper); }
  body { font-family: "Montserrat", Arial, sans-serif; color: var(--paper); }

  .brochure { position: relative; width: 1200px; height: 848px; overflow: hidden; background: var(--ink); }
  .backdrop { position: absolute; inset: 0; display: block; }

  .block { position: absolute; }
  .heading { font-weight: 800; text-transform: uppercase; letter-spacing: 0.2px; }

  .checklist { list-style: none; }
  .checklist li {
    position: relative; padding-left: 22px;
    font-size: 13.5px; font-weight: 600; line-height: 19.6px;
  }
  .checklist li::before {
    content: ""; position: absolute; left: 3px; top: 3px;
    width: 5px; height: 10px;
    border-right: 2.4px solid var(--tick, var(--brand-blue));
    border-bottom: 2.4px solid var(--tick, var(--brand-blue));
    transform: rotate(40deg);
  }

  /* Back cover */
  .why { left: 22px; top: 40px; width: 370px; }
  .why .heading { font-size: 26px; line-height: 32px; margin-bottom: 18px; }
  .license { left: 22px; top: 208px; font-size: 13.5px; line-height: 19.6px; color: var(--muted); }
  .divider { position: absolute; left: 22px; top: 320px; width: 358px; height: 1px; background: var(--rule); }
  .office { left: 22px; top: 353px; }
  .label { font-size: 14px; font-weight: 700; text-transform: uppercase; line-height: 20px; }
  .office .label { display: flex; align-items: center; gap: 5px; }
  .detail { font-size: 13.5px; line-height: 19.6px; color: var(--muted); }
  .office .detail { margin-top: 3px; }
  .contact { left: 22px; top: 411px; }
  .contact-line { display: flex; align-items: center; gap: 7px; padding-left: 2px; }
  .contact .label { margin-bottom: 3px; }
  .icon { flex: none; display: block; }
  .service-area { left: 22px; top: 490px; font-size: 14px; font-weight: 700; line-height: 20px; text-transform: uppercase; }

  /* Deck panel */
  .deck { left: 422px; top: 34px; width: 360px; }
  .deck .heading { font-size: 34px; line-height: 38px; margin-bottom: 18px; }
  .deck .checklist { --tick: var(--ink); }
  .deck .note { margin-top: 17px; font-size: 13.5px; line-height: 19.6px; }

  /* Gutter panel */
  .gutter { left: 826px; top: 625px; width: 360px; }
  .gutter .heading { font-size: 32px; line-height: 36px; margin-bottom: 12px; }
  .gutter .checklist { --tick: var(--paper); }
  .gutter .note { margin-top: 18px; font-size: 13.5px; line-height: 19.6px; color: var(--muted); }
</style>
</head>
<body>
<main class="brochure">
  <svg class="backdrop" width="1200" height="848" viewBox="0 0 1200 848" aria-hidden="false">
    <defs>
      <linearGradient id="framing-tones" x1="0" y1="0" x2="0" y2="1">
        <stop offset="0" stop-color="#b9d3e6"/>
        <stop offset="0.45" stop-color="#c79a6a"/>
        <stop offset="1" stop-color="#4a5c78"/>
      </linearGradient>
      <linearGradient id="roof-tones" x1="0" y1="0" x2="0" y2="1">
        <stop offset="0" stop-color="#2e3034"/>
        <stop offset="0.55" stop-color="#3a3b3f"/>
        <stop offset="1" stop-color="#8a5a35"/>
      </linearGradient>
      <linearGradient id="metal-roof-tones" x1="0" y1="0" x2="0" y2="1">
        <stop offset="0" stop-color="#e4e8ec"/>
        <stop offset="0.3" stop-color="#4b4f55"/>
        <stop offset="1" stop-color="#24262a"/>
      </linearGradient>
    </defs>

    <rect class="panel-back" x="0" y="0" width="400" height="848" fill="var(--ink)"/>
    <rect class="panel-deck" x="400" y="0" width="400" height="848" fill="var(--brand-blue)"/>

    <g role="img" aria-label="Photo: roofer with a hammer on a ladder building wooden roof framing">
      <polygon points="0,778 400,517 400,848 0,848" fill="url(#framing-tones)"/>
    </g>
    <g role="img" aria-label="Photo: two roofers installing a dark metal gutter along a standing-seam roof">
      <polygon points="400,517 800,256 800,848 400,848" fill="url(#roof-tones)"/>
    </g>
    <g role="img" aria-label="Photo: roofer in a hard hat working on a dark standing-seam metal roof">
      <rect x="800" y="0" width="400" height="848" fill="url(#metal-roof-tones)"/>
    </g>
    <polygon class="panel-gutter" points="800,400 1200,630 1200,848 800,848" fill="var(--ink)"/>

    <line x1="-4" y1="774" x2="804" y2="248" stroke="var(--paper)" stroke-width="9"/>
    <line x1="800" y1="400" x2="1204" y2="632" stroke="var(--paper)" stroke-width="7"/>
  </svg>

  <section class="block why">
    <h2 class="heading">Why Choose Bramble?</h2>
    <ul class="checklist">
      <li>HOA &amp; Commercial Specialists</li>
      <li>Fully Licensed &amp; Insured</li>
      <li>Reliable Scheduling</li>
      <li>Clear Communication</li>
      <li>Quality Materials &amp; Craftsmanship</li>
    </ul>
  </section>

  <div class="block license">
    <p>License Information:</p>
    <p>C-39 Roofing Contractor</p>
    <p>General B Contractor</p>
    <p>License #5372941</p>
  </div>

  <div class="divider"></div>

  <div class="block office">
    <p class="label">
      <svg class="icon" width="11" height="14" viewBox="0 0 11 14"><path d="M5.5 0C2.5 0 0 2.4 0 5.4 0 9.4 5.5 14 5.5 14S11 9.4 11 5.4C11 2.4 8.5 0 5.5 0Zm0 7.5a2.1 2.1 0 1 1 0-4.2 2.1 2.1 0 0 1 0 4.2Z" fill="var(--brand-blue)"/></svg>
      Office Location
    </p>
    <p class="detail">41 Tolliver Street, Suite D Irvine, CA 92604</p>
  </div>

  <div class="block contact">
    <p class="label">Contact Us Today for a Consultation</p>
    <p class="detail contact-line">
      <svg class="icon" width="13" height="13" viewBox="0 0 24 24"><path d="M6.6 10.8a15.1 15.1 0 0 0 6.6 6.6l2.2-2.2c.3-.3.7-.4 1-.2 1.1.4 2.3.6 3.6.6.6 0 1 .4 1 1V20c0 .6-.4 1-1 1A17 17 0 0 1 3 4c0-.6.4-1 1-1h3.5c.6 0 1 .4 1 1 0 1.3.2 2.5.6 3.6.1.3 0 .7-.2 1l-2.3 2.2Z" fill="none" stroke="var(--brand-blue)" stroke-width="2"/></svg>
      949-555-0162
    </p>
    <p class="detail contact-line">
      <svg class="icon" width="13" height="10" viewBox="0 0 13 10"><rect x="0" y="0" width="13" height="10" rx="1" fill="var(--brand-blue)"/><path d="M0.8 1 6.5 5.5 12.2 1" fill="none" stroke="var(--ink)" stroke-width="1.1"/></svg>
      rfp@bramblecrest.example
    </p>
  </div>

  <p class="block service-area">Serving Orange County &amp;<br>Surrounding Areas</p>

  <section class="block deck">
    <h2 class="heading">Deck &amp; Balcony<br>Services</h2>
    <ul class="checklist">
      <li>Balcony &amp; deck maintenance</li>
      <li>Deck resurfacing</li>
      <li>Small &amp; large deck repairs</li>
      <li>Full deck reconstruction</li>
    </ul>
    <p class="note">Specialized waterproofing solutions to keep decks safe, compliant, and durable.</p>
  </section>

  <section class="block gutter">
    <h2 class="heading">Gutter Services</h2>
    <ul class="checklist">
      <li>Small &amp; large gutter repairs</li>
      <li>Gutter cleaning &amp; maintenance</li>
      <li>New gutter installation &amp; replacement</li>
    </ul>
    <p class="note">Proper drainage protects your building—let us handle it.</p>
  </section>
</main>
</body>
</html>
```